Bookmark Design

We would like to design a book mark with logos of our two business and a quote.

One side with the quote "The first wealth is health" - Tobias Quill Harrow and the two logos.

The back side has the two logos with its respective phone numbers and a common address (this is to be advised to the winner of the project).

```html
<!DOCTYPE html>
<html lang="en">
<head>
<meta charset="utf-8">
<title>Bookmark – Front and Back</title>
<link rel="stylesheet" href="https://fonts.googleapis.com/css2?family=Bebas+Neue&family=Poppins:wght@500;600;700&display=swap">
<style>
  :root {
    --stage: #5e5e5e;
    --paper: #f7f7f7;
    --paper-shade: #e6e6e6;
    --green: #8dc63f;
    --leaf-green: #66b56a;
    --blue: #0b55a5;
    --ink: #555555;
    --band-grey: #6f6f6f;
  }
  * { margin: 0; padding: 0; box-sizing: border-box; }
  html, body { width: 1134px; height: 1200px; overflow: hidden; }
  body { background: var(--stage); position: relative; font-family: "Poppins", sans-serif; }

  .bookmark {
    position: absolute; top: 97px; width: 335px; height: 1005px;
    background: radial-gradient(ellipse at 50% 40%, var(--paper) 0%, #f1f1f1 60%, var(--paper-shade) 100%);
    overflow: hidden;
  }
  .bookmark--front { left: 176px; }
  .bookmark--back { left: 622px; }

  .backdrop { position: absolute; inset: 0 0 45px 0;
    background: radial-gradient(circle at 85% 8%, rgba(0,0,0,0.05), transparent 40%),
                radial-gradient(circle at 10% 92%, rgba(0,0,0,0.05), transparent 40%); }

  .footer-bands { position: absolute; left: 0; right: 0; bottom: 0; height: 43px; background: #ffffff; }
  .footer-bands .band-grey { position: absolute; top: 0; left: 0; right: 0; height: 11px; background: var(--band-grey); }
  .footer-bands .band-green { position: absolute; bottom: 0; left: 0; right: 0; height: 22px; background: var(--green); }

  .brand { position: absolute; left: 0; right: 0; display: flex; flex-direction: column; align-items: center; text-align: center; }
  .brand-dot { border-radius: 50%; flex-shrink: 0; }
  .brand-name { font-weight: 600; line-height: 1; white-space: nowrap; }
  .brand--clinic .brand-name { color: var(--blue); }
  .brand--dental .brand-name { color: var(--leaf-green); }

  .front-clinic { top: 63px; }
  .front-clinic .brand-dot { width: 68px; height: 68px; border: 2px solid var(--blue); margin-bottom: 10px; }
  .front-clinic .brand-name { font-size: 17px; }

  .front-dental { top: 895px; flex-direction: row; justify-content: center; gap: 8px; }
  .front-dental .brand-dot { width: 28px; height: 28px; background: var(--leaf-green); }
  .front-dental .brand-name { font-size: 20px; }

  .headline { position: absolute; inset: 0; font-family: "Bebas Neue", sans-serif; }
  .headline .green { fill: var(--green); }
  .headline .blue { fill: var(--blue); }

  .attribution { position: absolute; top: 834px; right: 34px; font-size: 17px; font-weight: 600; color: var(--ink); letter-spacing: -0.5px; }

  .back-clinic { top: 61px; }
  .back-clinic .brand-dot { width: 148px; height: 148px; border: 3px solid var(--blue); margin-bottom: 18px; }
  .back-clinic .brand-name { font-size: 30px; }

  .back-dental { top: 629px; flex-direction: row; justify-content: center; gap: 10px; padding: 0 20px; }
  .back-dental .brand-dot { width: 44px; height: 44px; background: var(--leaf-green); }
  .back-dental .brand-name { font-size: 27px; }

  .contact { position: absolute; left: 0; right: 0; display: flex; flex-direction: column; align-items: center; text-align: center; }
  .contact--clinic { top: 291px; }
  .contact--dental { top: 741px; }
  .icon { width: 34px; height: 34px; display: block; }
  .phone-number { font-family: "Bebas Neue", sans-serif; font-size: 60px; line-height: 1; color: var(--ink); margin-top: 4px; letter-spacing: 0.5px; }
  .contact .icon--pin { margin-top: 10px; }
  .address { font-size: 21px; font-weight: 500; line-height: 28px; color: var(--ink); margin-top: 2px; }
</style>
</head>
<body>

<section class="bookmark bookmark--front">
  <div class="backdrop" role="img" aria-label="Faint light grey leaf pattern"></div>

  <div class="brand brand--clinic front-clinic">
    <div class="brand-dot"></div>
    <div class="brand-name">ASHGROVE CLINIC</div>
  </div>

  <svg class="headline" viewBox="0 0 335 1005" width="335" height="1005" aria-label="The first wealth is health">
    <text class="green" x="35" y="333" font-size="221" textLength="267" lengthAdjust="spacingAndGlyphs">THE</text>
    <text class="green" x="35" y="450" font-size="147" textLength="267" lengthAdjust="spacingAndGlyphs">FIRST</text>
    <text class="blue" transform="translate(103 722) rotate(-90)" x="0" y="0" font-size="99" textLength="251" lengthAdjust="spacingAndGlyphs">WEALTH</text>
    <text class="green" x="120" y="725" font-size="371" textLength="182" lengthAdjust="spacingAndGlyphs">IS</text>
    <text class="blue" x="35" y="828" font-size="131" textLength="267" lengthAdjust="spacingAndGlyphs">HEALTH</text>
  </svg>

  <p class="attribution">- Tobias Quill Harrow</p>

  <div class="brand brand--dental front-dental">
    <div class="brand-dot"></div>
    <div class="brand-name">Harbour Dental</div>
  </div>

  <div class="footer-bands"><div class="band-grey"></div><div class="band-green"></div></div>
</section>

<section class="bookmark bookmark--back">
  <div class="backdrop" role="img" aria-label="Faint light grey leaf pattern"></div>

  <div class="brand brand--clinic back-clinic">
    <div class="brand-dot"></div>
    <div class="brand-name">ASHGROVE CLINIC</div>
  </div>

  <div class="contact contact--clinic">
    <svg class="icon icon--phone" viewBox="0 0 34 34" aria-hidden="true">
      <circle cx="17" cy="17" r="17" fill="var(--green)"/>
      <path d="M11 9.5c1-.8 2.2-.6 2.8.4l1.6 2.7c.5.9.2 1.8-.6 2.3l-1 .7c.8 1.9 2.2 3.5 4 4.6l.8-.9c.6-.7 1.6-.9 2.4-.3l2.5 1.8c.9.7 1 1.900.2 2.8l-1.1 1.1c-1.2 1.2-3.7.9-6.6-1.1-3.3-2.3-5.8-5.8-6.3-8.8-.3-1.8.2-3.5 1.3-4.3z" fill="#fff"/>
    </svg>
    <div class="phone-number">12345 54321</div>
    <svg class="icon icon--pin" viewBox="0 0 34 34" aria-hidden="true">
      <circle cx="17" cy="17" r="17" fill="var(--green)"/>
      <path d="M17 7.5c-3.6 0-6.3 2.7-6.3 6.2 0 4.3 6.3 11.3 6.3 11.3s6.3-7 6.3-11.3c0-3.5-2.7-6.2-6.3-6.2z" fill="#fff"/>
      <circle cx="17" cy="13.8" r="2.4" fill="var(--green)"/>
    </svg>
    <p class="address">Road name, State<br>City, Pin: 123459</p>
  </div>

  <div class="brand brand--dental back-dental">
    <div class="brand-dot"></div>
    <div class="brand-name">Harbour Dental</div>
  </div>

  <div class="contact contact--dental">
    <svg class="icon icon--phone" viewBox="0 0 34 34" aria-hidden="true">
      <circle cx="17" cy="17" r="17" fill="var(--green)"/>
      <path d="M11 9.5c1-.8 2.2-.6 2.8.4l1.6 2.7c.5.9.2 1.8-.6 2.3l-1 .7c.8 1.9 2.2 3.5 4 4.6l.8-.9c.6-.7 1.6-.9 2.4-.3l2.5 1.8c.9.7 1 1.9.2 2.8l-1.1 1.1c-1.2 1.2-3.7.9-6.6-1.1-3.3-2.3-5.8-5.8-6.3-8.8-.3-1.8.2-3.5 1.3-4.3z" fill="#fff"/>
    </svg>
    <div class="phone-number">12345 54321</div>
    <svg class="icon icon--pin" viewBox="0 0 34 34" aria-hidden="true">
      <circle cx="17" cy="17" r="17" fill="var(--green)"/>
      <path d="M17 7.5c-3.6 0-6.3 2.7-6.3 6.2 0 4.3 6.3 11.3 6.3 11.3s6.3-7 6.3-11.3c0-3.5-2.7-6.2-6.3-6.2z" fill="#fff"/>
      <circle cx="17" cy="13.8" r="2.4" fill="var(--green)"/>
    </svg>
    <p class="address">Road name, State<br>City, Pin: 123459</p>
  </div>

  <div class="footer-bands"><div class="band-grey"></div><div class="band-green"></div></div>
</section>

</body>
</html>
```